Vascular Secialist needs a tri-fold brochure

I would like to create a tri- fold of all the services that the vascular practice offers. The practice specializes in lower extremity vascular diseases. I would like to have the tri-fold have brief descriptions of all the services as well as images of the practice to show case the top of the line technology. The trip-fold will be front in back with a crisp modern design. The diseases that they treat are: arterial disease, venous disease, varicose veins, chronic venous insufficiency, deep vein thrombosis, uterine fibroids, pelvic and labial varicose veins, varicocele. Treatment options for all diseases that the practice treats.

Target Market(s)

Doctors

Industry/Entity Type

Medical

Font styles to use
Other font styles liked:
• Myriod Pro SemiExtende

Colors
33a6d7
86cae7
aaaaaa
85cae6
dcedf6
cee9f5
757575
9d9d9d
c3c3c3

Requirements
Must have
• creativity and taglines that capture the reader
Nice to have
• I would like the piece to mirror the website. www.larvinmesaclinic.com

```html
<!DOCTYPE html>
<html lang="en">
<head>
<meta charset="utf-8">
<title>Larvin Mesa Clinic – Tri-fold Brochure</title>
<link rel="stylesheet" href="https://fonts.googleapis.com/css2?family=Oswald:wght@400&family=Source+Sans+3:wght@400;600&display=swap">
<style>
  :root{
    --stage:#dcdcdc;
    --paper:#ffffff;
    --paper-grey:#f0f0f0;
    --ink:#2b2b2b;
    --ink-soft:#3a3a3a;
    --blue:#3f8fc4;
    --blue-light:#86bde0;
    --blue-deep:#6aaad6;
    --band-dark:#454545;
    --band-grey:#c3c3c3;
    --frame:#3b2417;
    --logo:#3b2a20;
  }
  *{margin:0;padding:0;box-sizing:border-box}
  html,body{width:1200px;height:1200px;overflow:hidden}
  body{background:var(--stage);position:relative;font-family:"Source Sans 3",Arial,sans-serif;color:var(--ink)}
  .brochure{position:absolute;left:37px;top:202px;width:1125px;height:795px;background:var(--paper);box-shadow:0 6px 18px rgba(0,0,0,.18)}
  .brochure__art{position:absolute;inset:0}
  .block{position:absolute}
  .body-copy{font-size:12.6px;line-height:16px;text-align:justify;color:var(--ink-soft)}
  .section-title{font-size:14px;font-weight:600;color:var(--ink)}
  .disease-title{font-size:13px;color:var(--blue)}
  .web-button{position:absolute;left:45px;top:665px;width:284px;height:40px;background:var(--blue-light);
    font-size:13px;letter-spacing:2.4px;color:var(--ink);display:flex;align-items:center;justify-content:center;
    box-shadow:0 8px 8px -6px rgba(0,0,0,.2)}
  .headline{font-family:"Oswald",Arial,sans-serif;text-align:center;color:var(--ink);letter-spacing:-.2px}
  .headline .accent{color:var(--blue)}
  .headline--mid{left:375px;width:375px;top:46px;font-size:24px;line-height:26px}
  .headline--mid .accent{color:#6fb0dc}
  .headline--tag{left:750px;width:375px;top:624px;font-size:27px;line-height:28.5px}
  .contact{left:375px;width:375px;top:540px;text-align:center;font-size:17px;line-height:22px}
  .contact__label{color:var(--ink)}
  .contact__value{color:#fff}
  .contact__group{margin-bottom:22px}
  .logo{left:750px;width:375px;top:74px;display:flex;align-items:center;justify-content:center;gap:14px}
  .logo__mark{width:22px;height:22px;border-radius:50%;background:var(--logo)}
  .logo__name{font-size:30px;letter-spacing:2px;color:var(--logo);font-weight:400}
</style>
</head>
<body>
<div class="brochure">
  <svg class="brochure__art" width="1125" height="795" viewBox="0 0 1125 795" xmlns="http://www.w3.org/2000/svg">
    <defs>
      <linearGradient id="lobbyFade" x1="0" y1="0" x2="1" y2="1">
        <stop offset="0" stop-color="#f7f7f7"/><stop offset="1" stop-color="#e6e8ea"/>
      </linearGradient>
      <linearGradient id="lobbyPhoto" x1="0" y1="0" x2="1" y2="1">
        <stop offset="0" stop-color="#c9d6df"/><stop offset=".5" stop-color="#e4e1da"/><stop offset="1" stop-color="#b9a48c"/>
      </linearGradient>
      <linearGradient id="portrait" x1="0" y1="0" x2="0" y2="1">
        <stop offset="0" stop-color="#b7c4a8"/><stop offset=".45" stop-color="#8e97b0"/><stop offset="1" stop-color="#5f6b8a"/>
      </linearGradient>
      <linearGradient id="contactBlue" x1="0" y1="0" x2="1" y2="1">
        <stop offset="0" stop-color="#9ccbe9"/><stop offset="1" stop-color="var(--blue-deep)"/>
      </linearGradient>
      <linearGradient id="sheen" x1="0" y1="0" x2="1" y2="0">
        <stop offset="0" stop-color="#e9e9e9"/><stop offset=".12" stop-color="#fbfbfb"/><stop offset="1" stop-color="#ffffff"/>
      </linearGradient>
    </defs>
    <!-- left panel -->
    <rect x="0" y="0" width="375" height="400" fill="url(#lobbyFade)" role="img" aria-label="Faint view of the clinic interior behind the text"/>
    <!-- middle panel -->
    <rect x="375" y="0" width="375" height="795" fill="var(--paper-grey)"/>
    <polygon points="375,302 750,135 750,158 375,320" fill="var(--blue-light)"/>
    <polygon points="375,320 750,158 750,548 375,465" fill="url(#lobbyPhoto)" role="img" aria-label="Photo of the bright clinic waiting room with window wall and seating"/>
    <polygon points="375,468 750,551 750,770 375,770" fill="url(#contactBlue)"/>
    <!-- right panel -->
    <rect x="750" y="0" width="375" height="795" fill="url(#sheen)"/>
    <rect x="791" y="178" width="298" height="440" fill="var(--frame)"/>
    <rect x="799" y="186" width="282" height="430" fill="url(#portrait)" role="img" aria-label="Portrait of the lead vascular surgeon in scrubs with arms crossed"/>
    <polygon points="750,550 1125,626 1125,770 750,770" fill="#ffffff"/>
    <line x1="750" y1="548" x2="1125" y2="624" stroke="#555" stroke-width="2"/>
    <!-- diagonal bands -->
    <polygon points="0,392 750,556 750,560 0,410" fill="#e4e4e4"/>
    <polygon points="0,392 750,556 750,760 0,760" fill="#ffffff" opacity="0"/>
    <polygon points="0,380 750,545 750,553 0,392" fill="var(--band-dark)"/>
    <polygon points="0,392 375,474 375,770 0,770" fill="#ffffff"/>
    <polygon points="0,392 375,474 375,480 0,408" fill="#e2e2e2"/>
    <!-- folds -->
    <line x1="375" y1="0" x2="375" y2="795" stroke="#d6d6d6"/>
    <line x1="750" y1="0" x2="750" y2="795" stroke="#d6d6d6"/>
    <!-- bottom strips -->
    <rect x="0" y="770" width="375" height="25" fill="var(--blue-light)"/>
    <rect x="375" y="770" width="375" height="25" fill="var(--band-dark)"/>
    <rect x="750" y="770" width="375" height="25" fill="var(--blue-light)"/>
  </svg>

  <!-- left panel content -->
  <p class="block body-copy" style="left:43px;top:38px;width:290px">Our conveniently located, state-of-art facility is designed for your patients comfort and utilizes cutting edge technology to provide minimally invasive treatments. Personable staff members make every visit a positive experience, with short wait times and an efficient, stream-lined process that ensures your patients leave feeling educated and confident that they are in good hands for all their vascular needs.</p>
  <h3 class="block section-title" style="left:43px;top:183px">Diseases we treat:</h3>
  <h4 class="block disease-title" style="left:43px;top:209px">Peripheral Arterial Disease</h4>
  <p class="block body-copy" style="left:43px;top:229px;width:290px">Peripheral Arterial Disease (PAD) develops when the arteries in the legs build up plaque, obstructing and narrowing the arteries and preventing blood, oxygen, glucose from flowing properly to tissue. This lack of blood-flow causes pain, cramping, and swelling in the legs as the muscles and tissue starve for blood and if untreated, can lead to amputation of the toes and/or foot.</p>
  <h4 class="block disease-title" style="left:43px;top:487px">Varicose Veins</h4>
  <p class="block body-copy" style="left:43px;top:511px;width:290px">Closely related to chronic venous insufficiency, varicose veins are enlarged veins that are visible through the skin. The veins often appear bulging or twisted and are generally larger than three millimeters in diameter. Varicose veins affect one out of two people over the age of 50, and women who have had children are particularly susceptible.</p>
  <div class="web-button">www.larvinmesaclinic.com</div>

  <!-- middle panel content -->
  <h2 class="block headline headline--mid">The Leading Vascular Surgery<br><span class="accent">Facility for Treating Arterial</span><br>Disease and Venous Disease.</h2>
  <div class="block contact">
    <div class="contact__group"><div class="contact__label">Call:</div><div class="contact__value">(555) 014-2736</div></div>
    <div class="contact__group"><div class="contact__label">Fax</div><div class="contact__value">(555) 014-2790</div></div>
    <div class="contact__group"><div class="contact__label">Address</div><div class="contact__value">2180 Alder Court<br>Larvin Mesa, CA 90210</div></div>
  </div>

  <!-- right panel content -->
  <div class="block logo"><span class="logo__mark"></span><span class="logo__name">LARVIN MESA CLINIC</span></div>
  <h1 class="block headline headline--tag">Leading vascular facility<br><span class="accent">specializing in treatment</span><br>of lower extremity arterial<br><span class="accent">and venous disease</span></h1>
</div>
</body>
</html>
```